Business Card Design

We need a business card for a new company in Sydney, Australia. The business supports the tourism industry, predominantly in the IT and systems area. The company focus is to assist business' to streamline their systems and processes, making the back end more efficient with the end goal making them more effective and profitable.

We would like a design that uses the colours red, white and possible black.

Target Market(s)

Tourism companies

Industry/Entity Type

Tourism

Contact Information for Business Card

Merin Quolly
VistaNode
Tel: (+61) 0487 215 964
Email: Merin@vistanode.com.au

Requirements
Nice to have
• Top right corner of the card rounded.

```html
<!DOCTYPE html>
<html lang="en">
<head>
<meta charset="utf-8">
<title>Merin Quolly VistaNode — Business Card</title>
<link rel="stylesheet" href="https://fonts.googleapis.com/css2?family=Coustard:wght@900&display=swap">
<style>
  :root {
    --card-white: #ffffff;
    --card-red: #ff0000;
    --card-black: #000000;
    --card-width: 1200px;
    --card-height: 741px;
  }

  * { box-sizing: border-box; margin: 0; padding: 0; }

  html, body {
    width: var(--card-width);
    height: var(--card-height);
    overflow: hidden;
    background: var(--card-white);
  }

  .business-card {
    position: relative;
    width: var(--card-width);
    height: var(--card-height);
    font-family: "Coustard", "Georgia", serif;
    font-weight: 900;
  }

  .card-artwork {
    position: absolute;
    inset: 0;
    display: block;
  }

  .brand-title {
    position: absolute;
    left: 0;
    right: 0;
    top: 338px;
    text-align: center;
    font-size: 62px;
    font-weight: 900;
    line-height: 1;
    letter-spacing: 2px;
    white-space: nowrap;
    color: var(--card-black);
    text-shadow:
      3px 0 0 var(--card-white), -3px 0 0 var(--card-white),
      0 3px 0 var(--card-white), 0 -3px 0 var(--card-white),
      2px 2px 0 var(--card-white), -2px -2px 0 var(--card-white),
      2px -2px 0 var(--card-white), -2px 2px 0 var(--card-white),
      3px 2px 0 var(--card-white), -3px -2px 0 var(--card-white),
      3px -2px 0 var(--card-white), -3px 2px 0 var(--card-white),
      5px 0 0 var(--card-black), -5px 0 0 var(--card-black),
      0 5px 0 var(--card-black), 0 -5px 0 var(--card-black),
      4px 4px 0 var(--card-black), -4px -4px 0 var(--card-black),
      4px -4px 0 var(--card-black), -4px 4px 0 var(--card-black);
  }

  .contact-details {
    position: absolute;
    left: 40px;
    top: 556px;
    list-style: none;
    font-size: 40px;
    line-height: 62px;
    letter-spacing: 1px;
    white-space: nowrap;
    color: var(--card-black);
    text-shadow:
      2px 0 0 var(--card-white), -2px 0 0 var(--card-white),
      0 2px 0 var(--card-white), 0 -2px 0 var(--card-white),
      2px 2px 0 var(--card-white), -2px -2px 0 var(--card-white),
      2px -2px 0 var(--card-white), -2px 2px 0 var(--card-white),
      4px 0 0 var(--card-black), -4px 0 0 var(--card-black),
      0 4px 0 var(--card-black), 0 -4px 0 var(--card-black),
      3px 3px 0 var(--card-black), -3px -3px 0 var(--card-black),
      3px -3px 0 var(--card-black), -3px 3px 0 var(--card-black);
  }
</style>
</head>
<body>
  <main class="business-card">
    <svg class="card-artwork" viewBox="0 0 1110 685" width="1200" height="741" aria-hidden="true">
      <path class="card-frame"
            d="M2 2 H1030 A78 78 0 0 1 1108 80 V683 H2 Z"
            fill="var(--card-white)" stroke="var(--card-black)" stroke-width="3"/>
      <polygon class="red-sash"
               points="12,12 490,12 760,455 1097,455 1097,670 615,670 415,345 348,230 12,230"
               fill="var(--card-red)"/>
      <polygon class="black-notch-top" points="490,12 615,12 555,113" fill="var(--card-black)"/>
      <polygon class="black-notch-bottom" points="493,670 615,670 555,572" fill="var(--card-black)"/>
      <polygon class="black-band-left" points="12,230 348,230 415,343 348,455 12,455" fill="var(--card-black)"/>
      <polygon class="black-band-right" points="1097,230 760,230 694,343 760,455 1097,455" fill="var(--card-black)"/>
    </svg>

    <svg class="card-artwork" viewBox="0 0 1110 685" width="1200" height="741">
      <defs>
        <linearGradient id="emblem-tone" x1="0" y1="0" x2="1" y2="0">
          <stop offset="0" stop-color="#ffffff"/>
          <stop offset="0.48" stop-color="#e6e6e6"/>
          <stop offset="0.52" stop-color="#111111"/>
          <stop offset="1" stop-color="#000000"/>
        </linearGradient>
      </defs>
      <rect class="emblem-area" x="712" y="35" width="293" height="160" rx="10"
            fill="url(#emblem-tone)" role="img"
            aria-label="Emblem of two interlocking puzzle pieces, one white and one black"/>
    </svg>

    <h1 class="brand-title">Merin Quolly VistaNode</h1>

    <ul class="contact-details">
      <li class="contact-phone">Tel : (+61) 0487 215 964</li>
      <li class="contact-email">Email : Merin @ vistanode.com.au</li>
    </ul>
  </main>
</body>
</html>
```